Vantor Cleaners Postcard - I would like to send this using MAIL to my prospects and current clients.

This store is under new management. I would like to design a high end postcard that showcases our services. Here is a list of the services that we provide to our customers.
- Premium Organic Dry Cleaning
- Laundered Shirts
- Expert Alterations
- Shoes and Leather Repairs by Pelham Brothers
- Area Rug Cleaning by Tarrick Cleaners
- Leather and Suede Cleaning by Mosk Cleaners
- Household Items
- Wedding Dress Cleaning and Preservation
I would like to offer 10% off (one-time use) coupon as well as 20% off to new customers.
Here is a logo file with location details.
While designing postcards, I would like to showcase stack of different garments (Season based) and household items. Also, use the colors that I have provided in the logo design.
We also offer Free Pick up and delivery.
About Us:
Vantor Cleaners is a premium dry cleaning and garment care service dedicated to delivering exceptional quality, convenience, and personalized attention. Located in the heart of Harlow Vale, we specialize in eco-friendly dry cleaning, expert stain removal, professional garment pressing, and specialized care for delicate fabrics, designer clothing, household items, and formal wear.
Our mission is to provide reliable, high-quality service while preserving the longevity and appearance of our customers’ garments. With state-of-the-art equipment, experienced staff, and a commitment to customer satisfaction, Vantor Cleaners ensures your clothing looks and feels its best — every time.
We also offer convenient services such as same-day cleaning, alterations, wash & fold, and pickup and delivery options, making garment care simple and hassle-free for our busy clientele.
Experience the difference with Vantor Cleaners — where luxury care meets everyday convenience.

Target Market(s)

Household above $100K

Industry/Entity Type

Dry Cleaning

Font styles to use
Serif

Colors
0054AA
0677BA
7BADD7
CADEEF
E8F1F8
FFC000
F8CF3A
FAE287
FDF2CF
FEFAEE

Requirements
Must have
• Elegant Design with stacked clothes, highlight Organic Dry Cleaning store. The color schemes should have these colors. D4AF37 (Fonts), 0D1B2A (Background). These are used in my logo and tagline.
Nice to have
• On the backside I would like to show our location on the map, streets

```html
<!DOCTYPE html>
<html lang="en">
<head>
<meta charset="utf-8">
<title>Vantor Cleaners Postcard</title>
<link rel="stylesheet" href="https://fonts.googleapis.com/css2?family=Cinzel:wght@400;600;700;800&family=Cormorant+Garamond:wght@500;600&family=Poppins:wght@300;400&display=swap">
<style>
  :root {
    --navy: #0D1B2A;
    --gold: #D4AF37;
    --gold-light: #F8CF3A;
    --gold-pale: #FAE287;
    --white: #ffffff;
    --ink: #1b1b1b;
    --page: #e4e4e4;
  }
  html, body {
    margin: 0;
    width: 1200px;
    height: 1117px;
    overflow: hidden;
    background: var(--page);
  }
  .sheet { position: relative; width: 1200px; height: 1117px; }
  .postcard {
    position: absolute;
    left: 210px;
    width: 780px;
    height: 520px;
    box-shadow: 0 6px 18px rgba(0,0,0,0.28);
  }
  .postcard--front { top: 25px; }
  .postcard--back { top: 572px; }
  .postcard svg { display: block; width: 780px; height: 520px; }

  .brand-name { font-family: "Cinzel", serif; font-weight: 600; fill: var(--gold); }
  .brand-tagline { font-family: "Cormorant Garamond", serif; font-weight: 500; fill: var(--gold); }
  .brand-address { font-family: "Cormorant Garamond", serif; font-weight: 500; fill: var(--gold); }

  .offer-gold { font-family: "Cinzel", serif; font-weight: 700; fill: url(#goldText); }
  .offer-white { font-family: "Cinzel", serif; font-weight: 600; fill: var(--white); }

  .headline { font-family: "Cinzel", serif; font-weight: 800; fill: url(#goldText); }
  .subline { font-family: "Cinzel", serif; font-weight: 600; fill: var(--white); }

  .services-title { font-family: "Cinzel", serif; font-weight: 700; fill: var(--navy); }
  .service-item { font-family: "Poppins", sans-serif; font-weight: 300; fill: var(--white); font-size: 11.6px; }
  .service-bullet { fill: var(--gold); }

  .delivery-lead { font-family: "Cinzel", serif; font-weight: 700; fill: var(--white); }
  .delivery-offer { font-family: "Cinzel", serif; font-weight: 700; fill: var(--gold); }

  .phone-number { font-family: "Cinzel", serif; font-weight: 700; fill: var(--ink); }
  .street-address { font-family: "Cinzel", serif; font-weight: 700; fill: var(--ink); }
  .about-heading { font-family: "Cinzel", serif; font-weight: 600; fill: var(--ink); }
  .about-copy { font-family: "Poppins", sans-serif; font-weight: 400; fill: var(--ink); font-size: 7.4px; }
</style>
</head>
<body>
<main class="sheet">

  <section class="postcard postcard--front">
    <svg viewBox="0 0 780 520" xmlns="http://www.w3.org/2000/svg">
      <defs>
        <linearGradient id="goldText" x1="0" y1="0" x2="0" y2="1">
          <stop offset="0" stop-color="#F8CF3A"/>
          <stop offset="0.55" stop-color="#D4AF37"/>
          <stop offset="1" stop-color="#a9851f"/>
        </linearGradient>
        <linearGradient id="goldStroke" x1="0" y1="0" x2="0" y2="1">
          <stop offset="0" stop-color="#FAE287"/>
          <stop offset="0.5" stop-color="#D4AF37"/>
          <stop offset="1" stop-color="#9c7a1a"/>
        </linearGradient>
        <linearGradient id="garmentTones" x1="0" y1="0" x2="1" y2="0">
          <stop offset="0" stop-color="#2b2f38"/>
          <stop offset="0.3" stop-color="#3b404b"/>
          <stop offset="0.45" stop-color="#7c63c8"/>
          <stop offset="0.58" stop-color="#3e6aa6"/>
          <stop offset="0.7" stop-color="#e5772a"/>
          <stop offset="0.82" stop-color="#4a78b4"/>
          <stop offset="1" stop-color="#e7c9b4"/>
        </linearGradient>
        <linearGradient id="photoFade" x1="0" y1="0" x2="0" y2="1">
          <stop offset="0" stop-color="#0D1B2A" stop-opacity="0"/>
          <stop offset="0.62" stop-color="#0D1B2A" stop-opacity="0"/>
          <stop offset="0.88" stop-color="#0D1B2A" stop-opacity="0.95"/>
          <stop offset="1" stop-color="#0D1B2A"/>
        </linearGradient>
      </defs>

      <rect width="780" height="520" fill="var(--navy)"/>

      <g class="garment-photo">
        <rect x="260" y="0" width="520" height="520" fill="url(#garmentTones)" role="img" aria-label="Photo of seasonal garments hanging on a clothing rail: puffer jackets, a purple sweater, denim, an orange top and a floral knit"/>
        <rect x="260" y="0" width="520" height="520" fill="url(#photoFade)"/>
      </g>

      <g class="brand-panel">
        <circle cx="160" cy="100" r="168" fill="var(--navy)"/>
        <path d="M0,170 H300 C352,270 350,420 288,520 H0 Z" fill="var(--navy)"/>
        <path d="M300,222 C352,305 350,430 282,520" fill="none" stroke="url(#goldStroke)" stroke-width="9"/>
        <path d="M0,128 L40,120 L40,142 L0,150 Z" fill="var(--gold)"/>
      </g>

      <g class="brand-block" text-anchor="middle">
        <text class="brand-name" x="162" y="100" font-size="32">VANTOR</text>
        <text class="brand-name" x="162" y="135" font-size="32">CLEANERS</text>
        <text class="brand-tagline" x="162" y="156" font-size="12">Refined Care For Every Garment</text>
        <text class="brand-address" x="162" y="177" font-size="12">18 Larkspur Hill Road</text>
        <text class="brand-address" x="162" y="192" font-size="12">Harlow Vale, HV 00214</text>
      </g>

      <g class="offers" text-anchor="middle">
        <text class="offer-gold" x="158" y="302" font-size="36">10% OFF</text>
        <text class="offer-white" x="158" y="322" font-size="13">(ONE-TIME USE)</text>
        <line x1="65" y1="340" x2="250" y2="340" stroke="var(--white)" stroke-width="1.2"/>
        <text class="offer-gold" x="140" y="426" font-size="82">20%</text>
        <text class="offer-white" x="212" y="440" font-size="22" text-anchor="start">OFF</text>
        <text class="offer-white" x="158" y="468" font-size="14.5">TO NEW CUSTOMERS.</text>
      </g>

      <g class="store-headline" text-anchor="middle">
        <text class="headline" x="528" y="460" font-size="60">PREMIUM</text>
        <text class="subline" x="528" y="494" font-size="27">DRY CLEANING STORE</text>
      </g>
    </svg>
  </section>

  <section class="postcard postcard--back">
    <svg viewBox="0 0 780 520" xmlns="http://www.w3.org/2000/svg">
      <defs>
        <linearGradient id="goldBand" x1="0" y1="0" x2="1" y2="0">
          <stop offset="0" stop-color="#b8921f"/>
          <stop offset="0.5" stop-color="#F8CF3A"/>
          <stop offset="1" stop-color="#D4AF37"/>
        </linearGradient>
        <linearGradient id="goldArc" x1="0" y1="0" x2="1" y2="0">
          <stop offset="0" stop-color="#FAE287"/>
          <stop offset="0.6" stop-color="#D4AF37"/>
          <stop offset="1" stop-color="#a9851f"/>
        </linearGradient>
        <linearGradient id="rackTones" x1="0" y1="0" x2="1" y2="0">
          <stop offset="0" stop-color="#c98a3a"/>
          <stop offset="0.35" stop-color="#e8e4dc"/>
          <stop offset="0.6" stop-color="#f3f1ec"/>
          <stop offset="0.8" stop-color="#233654"/>
          <stop offset="1" stop-color="#3b5478"/>
        </linearGradient>
        <linearGradient id="mapTones" x1="0" y1="0" x2="1" y2="1">
          <stop offset="0" stop-color="#d7eee3"/>
          <stop offset="0.5" stop-color="#f4eedc"/>
          <stop offset="1" stop-color="#d7eee3"/>
        </linearGradient>
      </defs>

      <rect width="780" height="520" fill="var(--white)"/>

      <path class="services-field" d="M0,0 H440 V190 C400,250 372,370 366,520 H0 Z" fill="var(--navy)"/>

      <g class="garment-photo">
        <path d="M410,0 H780 V120 C730,165 620,178 520,150 L410,120 Z" fill="url(#rackTones)" role="img" aria-label="Photo of shirts, blouses and jackets on wooden hangers along a clothing rail"/>
        <path d="M505,150 C610,185 728,170 780,118" fill="none" stroke="url(#goldArc)" stroke-width="8"/>
      </g>

      <g class="brand-block" text-anchor="middle">
        <circle cx="432" cy="98" r="70" fill="var(--navy)"/>
        <text class="brand-name" x="432" y="92" font-size="19">VANTOR</text>
        <text class="brand-name" x="432" y="113" font-size="19">CLEANERS</text>
        <text class="brand-tagline" x="432" y="126" font-size="7">Refined Care For Every Garment</text>
        <text class="brand-address" x="432" y="139" font-size="7">18 Larkspur Hill Road</text>
        <text class="brand-address" x="432" y="148" font-size="7">Harlow Vale, HV 00214</text>
      </g>

      <g class="services">
        <path d="M0,28 H262 A15 15 0 0 1 262,58 H0 Z" fill="url(#goldBand)"/>
        <text class="services-title" x="44" y="52" font-size="25">OUR SERVICES</text>
        <g class="service-list">
          <circle class="service-bullet" cx="50" cy="82" r="3.2"/><text class="service-item" x="61" y="86">Premium Organic Dry Cleaning</text>
          <circle class="service-bullet" cx="50" cy="100" r="3.2"/><text class="service-item" x="61" y="104">Laundered Shirts</text>
          <circle class="service-bullet" cx="50" cy="118" r="3.2"/><text class="service-item" x="61" y="122">Expert Alterations</text>
          <circle class="service-bullet" cx="50" cy="136" r="3.2"/><text class="service-item" x="61" y="140">Shoes and Leather Repairs by Pelham Brothers</text>
          <circle class="service-bullet" cx="50" cy="154" r="3.2"/><text class="service-item" x="61" y="158">Area Rug Cleaning by Tarrick Cleaners</text>
          <circle class="service-bullet" cx="50" cy="172" r="3.2"/><text class="service-item" x="61" y="176">Leather and Suede Cleaning by Mosk Cleaners</text>
          <circle class="service-bullet" cx="50" cy="190" r="3.2"/><text class="service-item" x="61" y="194">Household Items</text>
          <circle class="service-bullet" cx="50" cy="208" r="3.2"/><text class="service-item" x="61" y="212">Wedding Dress Cleaning and Preservation</text>
        </g>
      </g>

      <g class="delivery-offer-block">
        <rect x="52" y="246" width="44" height="44" rx="6" fill="none" stroke="var(--white)" stroke-width="2.4"/>
        <text class="delivery-lead" x="124" y="262" font-size="19">WE ALSO OFFER</text>
        <text class="delivery-offer" x="124" y="283" font-size="19">FREE PICK UP AND</text>
        <text class="delivery-offer" x="124" y="304" font-size="19">DELIVERY.</text>
      </g>

      <path class="location-map" d="M0,324 H370 C366,390 364,455 363,520 H0 Z" fill="url(#mapTones)" role="img" aria-label="Street map showing the store location with nearby roads"/>

      <g class="contact">
        <circle cx="443" cy="223" r="9" fill="none" stroke="var(--gold)" stroke-width="2.2"/>
        <path d="M439,218 q1,-1 2,0 l1.5,2.5 q0.5,1 -0.5,1.8 q1,2.5 3.5,3.8 q0.8,-1 1.8,-0.5 l2.5,1.5 q1,1 0,2 q-2,2 -4.5,0.5 q-5,-3 -7,-8 q-1,-2.5 0.7,-3.6 z" fill="var(--gold)"/>
        <text class="phone-number" x="458" y="236" font-size="32">55501-014-8832</text>
        <path d="M443,248 a4.5 4.5 0 1 1 9 0 c0,3.5 -4.5,8 -4.5,8 c0,0 -4.5,-4.5 -4.5,-8 z" fill="var(--gold)"/>
        <circle cx="447.5" cy="248" r="1.6" fill="var(--white)"/>
        <text class="street-address" x="458" y="256" font-size="10.5">214 Corwin Ave. Unit 3, Marden Falls, HV 002</text>
        <line x1="443" y1="270" x2="742" y2="270" stroke="var(--gold)" stroke-width="1.5"/>
      </g>

      <g class="about">
        <text class="about-heading" x="442" y="298" font-size="15">ABOUT US</text>
        <text class="about-copy">
          <tspan x="442" y="314">Vantor Cleaners is a premium dry cleaning and garment care service dedicated to</tspan>
          <tspan x="442" y="323">delivering exceptional quality, convenience, and personalized attention.</tspan>
          <tspan x="442" y="332">Located in the heart of Harlow Vale, we specialize in eco-friendly dry</tspan>
          <tspan x="442" y="341">cleaning, expert stain removal, professional garment pressing, and specialized</tspan>
          <tspan x="442" y="350">care for delicate fabrics, designer clothing, household items, and formal wear.</tspan>
          <tspan x="442" y="368">Our mission is to provide reliable, high-quality service while preserving</tspan>
          <tspan x="442" y="377">the longevity and appearance of our customers’ garments. With state-of-the-art</tspan>
          <tspan x="442" y="386">equipment, experienced staff, and a commitment to customer satisfaction,</tspan>
          <tspan x="442" y="395">Vantor Cleaners ensures your clothing looks and feels its best — every time.</tspan>
          <tspan x="442" y="413">We also offer convenient services such as same-day cleaning, alterations,</tspan>
          <tspan x="442" y="422">wash &amp; fold, and pickup and delivery options, making garment care simple and</tspan>
          <tspan x="442" y="431">hassle-free for our busy clientele.</tspan>
          <tspan x="442" y="449">Experience the difference with Vantor Cleaners — where luxury care meets</tspan>
          <tspan x="442" y="458">everyday convenience.</tspan>
        </text>
      </g>
    </svg>
  </section>

</main>
</body>
</html>
```